Health care technology software systems

We have a solid logo. We have company colors that will need to be used as well. We just need a great business card design. We sell to health plans but want to be modern
Updates

Need extra days to review

Target Market(s)

Health technology sector selling into Health Plans

Industry/Entity Type

Health Care Technology

Contact Information for Business Card

Name, title, address, phone number, email

Requirements
Must have
• Use of Kembrata corporate colors - Uploaded w/ our logos

```html
<!DOCTYPE html>
<html lang="en">
<head>
<meta charset="UTF-8">
<title>Kembrata Business Card</title>
<link rel="stylesheet" href="https://fonts.googleapis.com/css2?family=Montserrat:wght@300;400;500;600&display=swap">
<style>
  :root {
    --backdrop: #e9e9ec;
    --card-white: #f7f8f8;
    --brand-blue: #1089d0;
    --ink-dark: #232323;
    --navy: #1d3a8a;
    --leaf-green: #7ab829;
    --sky-blue: #1a8fd6;
    --soft-lavender: #c9c6e4;
    --silver: #d4d7dc;
  }
  * { margin: 0; padding: 0; box-sizing: border-box; }
  html, body {
    width: 1200px; height: 900px; overflow: hidden;
    background: var(--backdrop);
    font-family: "Montserrat", sans-serif;
  }
  .canvas {
    position: relative; width: 1200px; height: 900px;
    display: flex; flex-direction: column; align-items: center; justify-content: center;
    gap: 44px;
  }
  .card {
    position: relative; width: 620px; height: 354px; overflow: hidden;
    box-shadow: 0 6px 18px rgba(0,0,0,0.12);
  }
  .card--front { background: var(--card-white); }
  .card--back {
    background: var(--brand-blue);
    display: flex; align-items: center; justify-content: center; gap: 22px;
  }
  .deco-circle {
    position: absolute; right: -70px; top: 40px; width: 270px; height: 270px;
  }
  .brand {
    position: absolute; left: 56px; top: 96px;
    display: flex; align-items: center; gap: 16px;
  }
  .brand-dot {
    width: 40px; height: 40px; border-radius: 50%; background: var(--brand-blue);
  }
  .brand-name {
    font-weight: 300; font-size: 54px; letter-spacing: 1px; color: var(--ink-dark); line-height: 1;
  }
  .contact {
    position: absolute; left: 112px; top: 186px;
  }
  .person-name { font-size: 15px; font-weight: 400; color: var(--navy); }
  .person-role { font-size: 10px; font-weight: 400; color: var(--leaf-green); margin-top: 1px; }
  .contact-email { font-size: 15px; color: var(--sky-blue); margin-top: 18px; }
  .contact-phone { font-size: 15px; font-weight: 600; color: var(--navy); letter-spacing: 0.5px; }
  .contact-web { font-size: 15px; color: var(--sky-blue); margin-top: 14px; }
  .back-dot {
    width: 62px; height: 62px; border-radius: 50%; background: var(--silver);
  }
  .back-name {
    font-weight: 300; font-size: 72px; letter-spacing: 2px; color: var(--silver); line-height: 1;
  }
</style>
</head>
<body>
  <main class="canvas">
    <section class="card card--front">
      <svg class="deco-circle" viewBox="0 0 270 270" aria-hidden="true">
        <circle cx="135" cy="135" r="135" fill="var(--soft-lavender)" opacity="0.45"/>
      </svg>
      <div class="brand">
        <span class="brand-dot"></span>
        <span class="brand-name">kembrata</span>
      </div>
      <div class="contact">
        <p class="person-name">First Name Last Name</p>
        <p class="person-role">Position</p>
        <p class="contact-email">Name@website.com</p>
        <p class="contact-phone">000-000-0000</p>
        <p class="contact-web">www.website.com</p>
      </div>
    </section>
    <section class="card card--back">
      <span class="back-dot"></span>
      <span class="back-name">kembrata</span>
    </section>
  </main>
</body>
</html>
```